Solvatrix Basic Presentation of "Golden Horizon Collective"

I want this deck reviewed and reworked in a technical modern and compelling style...
Please see attachment.
Target Market(s)
European Industrie TOP-Management
Font styles to use
Sans Serif
Colors
85cae6
0255a3
ffffff
Requirements
Must have
- Compelling Design and clear wording
Nice to have
- Disruptive Innovation, Lean Management
Should not have
- arbitrariness

```html
<!DOCTYPE html>
<html lang="en">
<head>
<meta charset="utf-8">
<title>Solvatrix – Consulting &amp; Coaching Deck</title>
<link href="https://fonts.googleapis.com/css2?family=Libre+Baskerville:wght@400;700&family=Open+Sans:wght@300;400;600;700&display=swap" rel="stylesheet">
<style>
  :root{
    --navy:#131b4f;
    --sky:#85cae6;
    --line:#6fb8dc;
    --ink:#333844;
    --sheet:#ebebeb;
    --white:#ffffff;
    --label:#1b2456;
  }
  *{margin:0;padding:0;box-sizing:border-box}
  html,body{width:1200px;height:1200px;overflow:hidden;background:var(--sheet)}
  body{position:relative;font-family:"Open Sans",sans-serif;color:var(--ink)}
  .slide{position:absolute;width:548px;height:310px;background:var(--white);overflow:hidden;box-shadow:0 1px 5px rgba(0,0,0,.28)}
  .slide-label{position:absolute;width:548px;text-align:center;font-family:"Open Sans",sans-serif;font-size:24px;font-weight:400;color:var(--label);letter-spacing:.5px}
  .serif{font-family:"Libre Baskerville",serif}

  /* shared slide chrome */
  .header-rule{position:absolute;top:17px;left:0;width:378px;height:1px;background:var(--line)}
  .header-title{position:absolute;top:11px;left:386px;font-family:"Libre Baskerville",serif;font-weight:700;font-size:9.5px;color:var(--navy);white-space:nowrap}
  .pill{position:absolute;left:0;height:12px;background:var(--navy);color:var(--white);font-size:7.4px;font-weight:700;line-height:12px;padding-left:17px;border-radius:0 7px 7px 0;white-space:nowrap}
  .body-text{position:absolute;left:16px;font-size:6.4px;line-height:10px;color:var(--ink)}
  .footer-bar{position:absolute;left:0;top:291px;width:130px;height:6px;background:var(--navy);color:var(--white);font-size:5px;letter-spacing:1.6px;line-height:6px;padding-left:16px}
  .footer-seal{position:absolute;top:285px;left:132px;width:18px;height:18px;border-radius:50%;background:var(--navy);border:2px solid var(--white);box-shadow:0 0 0 1px var(--navy)}
  .page-no{position:absolute;top:291px;right:16px;font-size:5.5px;color:var(--ink)}

  /* name seal */
  .seal{position:absolute;border-radius:50%;background:var(--navy);display:flex;align-items:center;justify-content:center;color:var(--white);font-family:"Libre Baskerville",serif;font-weight:400;box-shadow:0 0 0 3px var(--white),0 0 0 4px var(--sky)}

  /* cover */
  .cover-bg{position:absolute;inset:0;background:linear-gradient(180deg,#f6f7f8 0%,#e3e5e7 35%,#d2d5d8 50%,#eef0f1 62%)}
  .cover-band{position:absolute;left:0;top:155px;width:548px;height:155px;background:var(--navy)}
  .cover-title{position:absolute;top:16px;width:100%;text-align:center;font-family:"Libre Baskerville",serif;font-weight:700;font-size:18.5px;color:var(--navy)}
  .cover-url{position:absolute;top:40px;width:100%;text-align:center;font-size:6.5px;letter-spacing:2.6px;color:var(--navy)}
  .cover-rule{position:absolute;left:0;width:548px;height:1px;background:#8a93b8}
  .cover-tagline{position:absolute;top:268px;width:100%;text-align:center;font-family:"Libre Baskerville",serif;font-weight:700;font-size:13.6px;color:var(--white);white-space:nowrap}

  /* page 01 */
  .scale-title{position:absolute;top:133px;left:0;width:548px;text-align:center;font-size:7.6px;font-weight:600;color:#222}
  .branch-label{position:absolute;top:196px;width:70px;margin-left:-35px;text-align:center;font-size:6.2px;line-height:8.5px;color:#444}

  /* page 02 */
  .photo-arrow{position:absolute;left:393px;top:46px;width:136px;height:264px;background:linear-gradient(180deg,#2d7f92 0%,#1f5e70 45%,#7c8c83 70%,#6b7d77 100%);border-radius:4px}

  /* page 03 */
  .surf-photo{position:absolute;left:0;top:190px;width:548px;height:120px;background:linear-gradient(180deg,rgba(255,255,255,1) 0%,#cfe0e6 30%,#6f9aa8 60%,#3f6e7e 100%)}

  /* back page */
  .back-bg{position:absolute;inset:0;background:radial-gradient(ellipse at 50% 60%,#dfe8ec 0%,#f2f6f7 55%,#fbfcfc 100%)}
  .back-accent{position:absolute;left:0;top:220px;width:12px;height:64px;background:var(--sky)}
  .contact{position:absolute;width:100%;text-align:center;color:var(--navy)}
  .dot{display:inline-block;width:7px;height:7px;border-radius:50%;background:var(--navy);margin:0 1px}
</style>
</head>
<body>

<!-- Cover -->
<section class="slide" style="left:22px;top:36px">
  <div class="cover-bg" role="img" aria-label="Soft grey photograph of a breaking ocean wave"></div>
  <div class="cover-band"></div>
  <div class="cover-title">CONSULTING &amp; COACHING</div>
  <div class="cover-url">www.solvatrix-cc.com</div>
  <div class="seal" style="left:178px;top:60px;width:192px;height:192px;font-size:27px">Solvatrix</div>
  <div class="cover-rule" style="top:265px"></div>
  <div class="cover-tagline">DIGITALIZATION, MANAGEMENT OF CHANGE AND COACHING</div>
  <div class="cover-rule" style="top:287px"></div>
</section>
<div class="slide-label" style="left:22px;top:360px">COVER PAGE</div>

<!-- Page 01 -->
<section class="slide" style="left:632px;top:36px">
  <div class="header-rule"></div>
  <div class="header-title">CONSULTING &amp; COACHING</div>
  <div class="pill" style="top:40px;width:196px">ACCELERATING NOVA ERP PROJECTS</div>
  <div class="body-text" style="top:62px;font-size:6px">ILLUMINATING THE BLIND SPOTS - MAKING NOVA ERP PROJECTS CHALLENGING.</div>
  <div class="scale-title">SCALE IDEAS FOR THE CREATION OF EXPONENTIAL GROWTH WITHIN YOUR ORGANIZATION</div>
  <svg style="position:absolute;left:0;top:0" width="548" height="310">
    <g stroke="#6fb8dc" stroke-width="1" fill="none">
      <line x1="274" y1="146" x2="274" y2="160"/>
      <line x1="38" y1="160" x2="510" y2="160"/>
      <line x1="38" y1="160" x2="38" y2="190"/>
      <line x1="96" y1="160" x2="96" y2="190"/>
      <line x1="158" y1="160" x2="158" y2="190"/>
      <line x1="217" y1="160" x2="217" y2="190"/>
      <line x1="274" y1="160" x2="274" y2="190"/>
      <line x1="337" y1="160" x2="337" y2="190"/>
      <line x1="396" y1="160" x2="396" y2="190"/>
      <line x1="453" y1="160" x2="453" y2="190"/>
      <line x1="510" y1="160" x2="510" y2="190"/>
    </g>
  </svg>
  <div class="branch-label" style="left:38px">Staff experts<br>on demand</div>
  <div class="branch-label" style="left:96px">Community<br>&amp; Crowd</div>
  <div class="branch-label" style="left:158px">Algorithm</div>
  <div class="branch-label" style="left:217px">Leveraged<br>assets</div>
  <div class="branch-label" style="left:274px">Interface<br>processes</div>
  <div class="branch-label" style="left:337px">Dashboards</div>
  <div class="branch-label" style="left:396px">Ex-<br>perimetation</div>
  <div class="branch-label" style="left:453px">Autonomy<br>of teams</div>
  <div class="branch-label" style="left:510px">Social<br>Technologies</div>
  <div class="footer-bar">www.solvatrix-cc.com</div>
  <div class="footer-seal"></div>
  <div class="page-no">01</div>
</section>
<div class="slide-label" style="left:632px;top:360px">PAGE - 01</div>

<!-- Page 02 -->
<section class="slide" style="left:22px;top:424px">
  <div class="header-rule"></div>
  <div class="header-title">CONSULTING &amp; COACHING</div>
  <div class="pill" style="top:53px;width:186px">WHERE ARE WE ARE COMING FROM?</div>
  <div class="body-text" style="top:72px">Why are we here, today?</div>
  <div class="pill" style="top:108px;width:362px">WHAT DOES NOVA ERP MEAN FOR OUR DAILY BUSINESS- &amp; PROJECT LIVES?</div>
  <div class="body-text" style="top:127px">What makes the management of change so difficult – and how to solve the issue.</div>
  <div class="pill" style="top:165px;width:378px">HOW WE SOLVE THE OCCURRING CHALLENGES DURING AN NOVA ERP PROJECT</div>
  <div class="body-text" style="top:184px">Digitalization is “real-timification” (or: zero latency) of all our businesses and collaborations.</div>
  <div class="body-text" style="top:205px">“embedded Management of Change”</div>
  <div class="body-text" style="top:226px;width:370px">An introduction on the economical background, on the implementation concepts and the mind set of NOVA ERP projects – and how that affects an organization implementing.</div>
  <div class="photo-arrow" role="img" aria-label="Photograph of a surfer riding a blue ocean wave"></div>
  <div class="footer-bar">www.solvatrix-cc.com</div>
  <div class="footer-seal"></div>
  <div class="page-no">02</div>
</section>
<div class="slide-label" style="left:22px;top:750px">PAGE - 02</div>

<!-- Page 03 -->
<section class="slide" style="left:632px;top:424px">
  <div class="surf-photo" role="img" aria-label="Motion-blurred photograph of a surfer on a teal wave"></div>
  <div class="header-rule"></div>
  <div class="header-title">CONSULTING &amp; COACHING</div>
  <div class="pill" style="top:38px;width:80px">PREAMBLE</div>
  <div class="body-text" style="top:56px;font-size:7.4px;font-weight:600">Es ist echt irre, was unser Gehirn alles so schafft! - Viel Spaß beim Lesen !!!</div>
  <div class="body-text" style="top:78px;width:518px;font-size:6.2px;line-height:10.2px">Erstaunlich, was unser Gehirn alles leisten kann. Buchstaben dürfen durcheinander stehen, solange der erste und der letzte Buchstabe an der richtigen Stelle sind. Der Text bleibt trotzdem lesbar, weil wir nicht jeden Buchstaben einzeln lesen, sondern das Wort als Ganzes erkennen. Echt krass! Das geht wirklich! Und dafür gab es früher jahrelang Unterricht.</div>
  <div class="body-text" style="top:128px;font-size:7.4px;font-weight:600">Und als absolute Steigerung dieses hier -</div>
  <div class="body-text" style="top:149px;width:518px;font-size:6.2px;line-height:10.2px">D1E5E M1TT31LUNG Z31GT D1R, ZU W3LCH3N L315TUNG3N UN53R G3H1RN F43H1G 15T. 4M 4NF4NG W4R 35 5CHW3R, D4NN G1NG 35 L31CHT3R. N4CH K4UM 31N3R Z31L3 L1E5T D31N G3H1RN 4UTOM4T15CH M1T. 5T4RK, OD3R?</div>
  <div class="footer-bar">www.solvatrix-cc.com</div>
  <div class="footer-seal"></div>
  <div class="page-no">03</div>
</section>
<div class="slide-label" style="left:632px;top:750px">PAGE - 03</div>

<!-- Back page -->
<section class="slide" style="left:22px;top:816px">
  <div class="back-bg" role="img" aria-label="Faded photograph of ocean spray and a surfer"></div>
  <div class="back-accent"></div>
  <div class="seal" style="left:198px;top:24px;width:152px;height:152px;font-size:22px">Solvatrix</div>
  <svg style="position:absolute;left:262px;top:180px" width="26" height="10"><polyline points="1,2 13,8 25,2" fill="none" stroke="#131b4f" stroke-width="1.6"/></svg>
  <div class="contact serif" style="top:212px;font-size:10.5px">Contact Us</div>
  <div class="contact" style="top:232px;line-height:7px"><span class="dot"></span><span class="dot"></span><span class="dot"></span></div>
  <div class="contact" style="top:249px;font-size:5.6px;letter-spacing:.3px">M. Brenner-Valli, CH - 8000 Zürich / Schweiz</div>
  <div class="contact" style="top:266px;font-size:5.6px;letter-spacing:.3px">Lukas (at) Brennervalli.net</div>
  <div class="contact" style="top:283px;font-size:5.6px;letter-spacing:.3px">www.solvatrix-cc.com</div>
</section>
<div class="slide-label" style="left:22px;top:1141px">BACK PAGE</div>

<!-- Seal -->
<div class="seal" style="left:782px;top:846px;width:248px;height:248px;font-size:36px;box-shadow:none">Solvatrix</div>

</body>
</html>
```